Lend a Lantern Website Design (design layout only)

We need a website design for a new nonprofit organization based in Des Moines, Iowa called Lend a Lantern. The nonprofit provides soccer training opportunities to youth soccer players looking to improve their game while also affecting the lives of the less fortunate in a positive way. While participating in the training programs the players also go out and raise money for selected charities. The organization then donates the funds. In its first 18 months we donated $10,500. We would like to see designs attempt to symbolize the mission of the nonprofit - essentially "improve you while improving someone else."

We would like to see the following features:

· A place to donate - Our intent is to have the home page linked to the donation page; a simple straight-forward process for people to give money, and make donating as painless as possible - no account needed to make a donation, credit card or e-check should be the only information needed to donate, and have it be on a single page.

· A photo gallery so people can browse the photo gallery to get a better understanding of our organization and a place to add videos and a calendar to show upcoming events

· A place for contact information and the profiles of directors and board members. This should include a spot showing all the charities the organization donates to. Also includes a news section/blog for comments and suggestions.

We want the design to revolve around the content and mission. We would really like to stress our organization as nonprofit. We would also like if the website was user friendly and easy to navigate.

The logo of our organization is uploaded

```html
<!DOCTYPE html>
<html lang="en">
<head>
<meta charset="utf-8">
<title>Lend a Lantern</title>
<link href="https://fonts.googleapis.com/css2?family=Ubuntu:wght@400;500;700&family=Lora:ital@1&display=swap" rel="stylesheet">
<style>
:root{
  --green:#5cb82e;
  --green-bright:#6ab23a;
  --green-dark:#2d5418;
  --heading:#2f4f14;
  --text:#555;
  --text-dark:#333;
  --line:#e2e2e2;
  --footer:#151716;
  --footer-bar:#3f5c2c;
  --white:#fff;
}
*{margin:0;padding:0;box-sizing:border-box}
html,body{width:1200px;height:2595px;overflow:hidden}
body{background:var(--white);font-family:"Ubuntu",sans-serif;color:var(--text);position:relative}
.abs{position:absolute}
/* header */
.site-header{position:absolute;left:0;top:0;width:1200px;height:112px;background:var(--white)}
.brand{position:absolute;left:140px;top:34px;display:flex;align-items:center;gap:10px}
.brand-mark{width:30px;height:30px;background:var(--green-dark);border-radius:50%}
.brand-name{font-weight:700;font-size:22px;color:var(--green-dark)}
.main-nav{position:absolute;top:52px;left:428px;display:flex;gap:38px;font-size:17px;font-weight:500;color:var(--text-dark);letter-spacing:.5px}
.main-nav .active{color:var(--green-bright)}
/* hero */
.hero{position:absolute;left:0;top:112px;width:1200px;height:488px;background:linear-gradient(135deg,#b89a3a 0%,#5a6f8f 30%,#5fa0d0 60%,#c69a78 85%,#7e8fa8 100%)}
.btn-donate{position:absolute;left:465px;top:568px;width:270px;height:64px;border-radius:32px;background:var(--green);color:var(--white);font-weight:700;font-size:28px;display:flex;align-items:center;justify-content:center;box-shadow:0 0 0 5px #fff,0 4px 8px 5px rgba(0,0,0,.18)}
/* welcome */
.welcome{position:absolute;left:140px;top:676px;width:500px}
.welcome-kicker{font-family:"Lora",serif;font-style:italic;font-size:19px;color:var(--text-dark)}
.welcome-title{font-weight:700;font-size:29px;color:var(--heading);margin-top:-2px}
.welcome p{font-size:14.5px;line-height:24px;margin-top:10px}
.welcome p + p{margin-top:28px}
.video{position:absolute;left:672px;top:694px;width:383px;height:279px;background:linear-gradient(160deg,#4a4a4a,#2a2a2a);border:4px solid #f1f1f1;box-shadow:0 0 4px rgba(0,0,0,.2)}
.video svg{position:absolute;left:165px;top:113px}
.divider{position:absolute;left:140px;width:920px;height:30px;background:radial-gradient(ellipse at top,rgba(0,0,0,.08),rgba(0,0,0,0) 70%)}
/* section headings */
.section-title{position:absolute;font-weight:700;font-size:29px;color:var(--heading)}
.pill{position:absolute;height:28px;padding:0 16px;border-radius:14px;background:var(--green);color:var(--white);font-size:13px;display:flex;align-items:center}
/* gallery */
.gallery{position:absolute;left:140px;top:1124px;width:584px;height:281px;display:grid;grid-template-columns:repeat(4,1fr);grid-template-rows:repeat(2,1fr);gap:3px}
.gallery .photo{background:linear-gradient(150deg,#d9d2c5,#7d9ab5 60%,#c3a88a)}
.gallery .photo:nth-child(2n){background:linear-gradient(150deg,#e8e2d2,#b8a890 50%,#8e9db0)}
.gallery .photo:nth-child(3n){background:linear-gradient(150deg,#cfd6de,#9aa6b2 55%,#d6c0a5)}
/* calendar */
.calendar{position:absolute;left:778px;top:1124px;width:281px;border:1px solid #ddd;font-size:13px}
.cal-head{height:46px;background:var(--green);color:var(--white);display:flex;align-items:center;justify-content:space-between;padding:0 12px;font-size:17px;font-weight:500}
.cal-grid{display:grid;grid-template-columns:repeat(7,1fr)}
.cal-grid span{height:36px;display:flex;align-items:center;justify-content:center;border-right:1px solid #e6e6e6;border-bottom:1px solid #e6e6e6;color:var(--text-dark)}
.cal-grid span:nth-child(7n){border-right:0}
.cal-grid .dow{font-weight:700;background:#fff}
.cal-grid .day{background:#f3f3f3}
.cal-grid .empty{background:#fff}
.cal-grid .mark{background:var(--green);color:var(--white)}
/* team */
.member{position:absolute;width:440px;height:151px}
.member .avatar{position:absolute;left:0;top:0;width:151px;height:151px;border-radius:50%;border:5px solid #fff;box-shadow:0 0 6px rgba(0,0,0,.25);background:radial-gradient(circle at 50% 40%,#e3c9b0,#8aa3bd 70%)}
.member h3{position:absolute;left:171px;top:16px;font-size:16px;font-weight:700;color:var(--heading)}
.member h3 small{font-weight:400;color:var(--text);font-size:15px}
.member p{position:absolute;left:171px;top:42px;width:270px;font-size:15px;line-height:24px}
.team-vline{position:absolute;left:600px;top:1589px;width:1px;height:400px;background:var(--line)}
.team-hline{position:absolute;top:1773px;height:1px;background:var(--line)}
/* footer */
.site-footer{position:absolute;left:0;top:2076px;width:1200px;height:449px;background:var(--footer);color:var(--white)}
.foot-title{position:absolute;font-size:19px;font-weight:500}
.foot-links{position:absolute;left:140px;top:98px;list-style:none;font-size:13px;font-weight:500}
.foot-links li{height:35px;padding-left:18px;position:relative}
.foot-links li::before{content:"›";position:absolute;left:0;top:-2px;color:#aaa}
.news-item{position:absolute;left:357px;width:316px;height:100px;border-bottom:1px solid #444}
.news-item .thumb{position:absolute;left:0;top:0;width:65px;height:65px;border:2px solid #fff;background:linear-gradient(150deg,#d9cbb6,#7f9cb6)}
.news-item h4{position:absolute;left:86px;top:-2px;font-size:14px;font-weight:700}
.news-item p{position:absolute;left:86px;top:20px;width:230px;font-size:13px;line-height:21px;font-weight:500}
.news-item p b{color:var(--green);font-weight:500}
.contact-row{position:absolute;left:763px;display:flex;gap:18px;font-size:13px;font-weight:500;line-height:20px}
.contact-row svg{flex:none;margin-top:2px}
.contact-row a{color:var(--green);text-decoration:none}
.subscribe{position:absolute;left:768px;top:2462px;width:240px;height:2px;background:var(--green)}
.bottom-bar{position:absolute;left:0;top:2525px;width:1200px;height:70px;background:var(--footer-bar);color:var(--white)}
.copyright{position:absolute;left:140px;top:28px;font-size:12px;font-weight:500}
.socials{position:absolute;left:886px;top:20px;display:flex;gap:9px}
.socials span{width:28px;height:28px;border-radius:50%;background:#8a9a7e}
</style>
</head>
<body>

<header class="site-header">
  <div class="brand"><span class="brand-mark"></span><span class="brand-name">Lend a Lantern</span></div>
  <nav class="main-nav">
    <span class="active">HOME</span><span>ABOUT</span><span>SERVICES</span><span>PLAYER</span><span>DONATION</span><span>CONTACT US</span>
  </nav>
</header>

<div class="hero" role="img" aria-label="Coach explaining a play on a clipboard to young players gathered in a locker room"></div>
<div class="btn-donate">DONATION NOW</div>

<section class="welcome">
  <div class="welcome-kicker">Welcome to</div>
  <h1 class="welcome-title">LEND A LANTERN</h1>
  <p>Lorem Ipsum is simply dummy text of the printing and typesetting industry. Lorem Ipsum has been the industry's standard dummy text ever since the 1500s, when an unknown printer took a galley of type and scrambled it to make a type specimen book. It has survived not only five centuries, but also the leap into electronic typesetting, remaining essentially</p>
  <p>Lorem Ipsum is simply dummy text of the printing and typesetting industry. Lorem Ipsum has been the industry's standard dummy text when an unknown printer took a galley.</p>
</section>
<div class="video" role="img" aria-label="Video still of smiling volunteers in matching shirts">
  <svg width="52" height="52" viewBox="0 0 52 52"><circle cx="26" cy="26" r="23" fill="none" stroke="#fff" stroke-width="3"/><path d="M21 16 L36 26 L21 36 Z" fill="#fff"/></svg>
</div>

<div class="divider" style="top:1027px"></div>

<h2 class="section-title" style="left:140px;top:1064px">PHOTO GALLERY</h2>
<div class="pill" style="left:605px;top:1077px">View All Photos</div>
<div class="gallery">
  <div class="photo" role="img" aria-label="Team meeting around a table"></div>
  <div class="photo" role="img" aria-label="Volunteers in matching shirts"></div>
  <div class="photo" role="img" aria-label="Board member portrait"></div>
  <div class="photo" role="img" aria-label="Volunteer at a desk"></div>
  <div class="photo" role="img" aria-label="Board member portrait"></div>
  <div class="photo" role="img" aria-label="Smiling volunteer"></div>
  <div class="photo" role="img" aria-label="Volunteers in matching shirts"></div>
  <div class="photo" role="img" aria-label="Team meeting around a table"></div>
</div>

<h2 class="section-title" style="left:778px;top:1064px">UPCOMING EVENTS</h2>
<div class="calendar">
  <div class="cal-head">
    <svg width="12" height="16" viewBox="0 0 12 16"><path d="M10 2 L3 8 L10 14" fill="none" stroke="#fff" stroke-width="2.5"/></svg>
    <span>JULY 2014</span>
    <svg width="12" height="16" viewBox="0 0 12 16"><path d="M2 2 L9 8 L2 14" fill="none" stroke="#fff" stroke-width="2.5"/></svg>
  </div>
  <div class="cal-grid">
    <span class="dow">Su</span><span class="dow">Mo</span><span class="dow">Tu</span><span class="dow">We</span><span class="dow">Th</span><span class="dow">Fr</span><span class="dow">Sa</span>
    <span class="empty"></span><span class="empty"></span><span class="day">1</span><span class="day">2</span><span class="day">3</span><span class="day">4</span><span class="day">5</span>
    <span class="day">6</span><span class="day">7</span><span class="day">8</span><span class="day">9</span><span class="day">10</span><span class="day">11</span><span class="day">12</span>
    <span class="day">13</span><span class="day">14</span><span class="day">15</span><span class="day">16</span><span class="day">17</span><span class="day">18</span><span class="day">19</span>
    <span class="day">20</span><span class="day">21</span><span class="day">22</span><span class="day">23</span><span class="day mark">24</span><span class="day">25</span><span class="day">26</span>
    <span class="day">27</span><span class="day">28</span><span class="day mark">29</span><span class="day">30</span><span class="day">31</span><span class="empty"></span><span class="empty"></span>
  </div>
</div>

<div class="divider" style="top:1470px"></div>

<h2 class="section-title" style="left:140px;top:1508px">OUR TEAM</h2>
<div class="pill" style="left:948px;top:1514px">View All Team</div>

<div class="member" style="left:140px;top:1589px">
  <div class="avatar" role="img" aria-label="Portrait of the director"></div>
  <h3>Jon Doe <small>-Director</small></h3>
  <p>Lorem Ipsum is simply dummy text of the printing and typesetting industry. Lorem Ipsum has been</p>
</div>
<div class="member" style="left:631px;top:1589px">
  <div class="avatar" role="img" aria-label="Portrait of a board member"></div>
  <h3>Member Name</h3>
  <p>Lorem Ipsum is simply dummy text of the printing and typesetting industry. Lorem Ipsum has been</p>
</div>
<div class="member" style="left:140px;top:1838px">
  <div class="avatar" role="img" aria-label="Portrait of the director"></div>
  <h3>Jon Doe <small>-Director</small></h3>
  <p>Lorem Ipsum is simply dummy text of the printing and typesetting industry. Lorem Ipsum has been</p>
</div>
<div class="member" style="left:631px;top:1838px">
  <div class="avatar" role="img" aria-label="Portrait of a board member"></div>
  <h3>Member Name</h3>
  <p>Lorem Ipsum is simply dummy text of the printing and typesetting industry. Lorem Ipsum has been</p>
</div>
<div class="team-vline"></div>
<div class="team-hline" style="left:140px;width:430px"></div>
<div class="team-hline" style="left:631px;width:428px"></div>

<footer class="site-footer">
  <div class="foot-title" style="left:140px;top:44px">Support/Help</div>
  <ul class="foot-links">
    <li>Home</li><li>About</li><li>Services</li><li>Player</li><li>donation</li><li>Contact Us</li>
  </ul>

  <div class="foot-title" style="left:357px;top:40px">Latest News</div>
  <div class="news-item" style="top:102px">
    <div class="thumb" role="img" aria-label="News photo"></div>
    <h4>Lorem ipsum dolo consectetur elit</h4>
    <p>Sed ut perspiciatis unde omnis iste natus error sit voluptatem accusantium...<b>Read more</b></p>
  </div>
  <div class="news-item" style="top:222px">
    <div class="thumb" role="img" aria-label="News photo"></div>
    <h4>Lorem ipsum dolo consectetur elit</h4>
    <p>Sed ut perspiciatis unde omnis iste natus error...<b>Read more</b></p>
  </div>
  <div class="news-item" style="top:333px;border-bottom:0">
    <div class="thumb" role="img" aria-label="News photo"></div>
    <h4>Lorem ipsum dolo consectetur elit</h4>
    <p>Sed ut perspiciatis unde omnis iste natus error...<b>Read more</b></p>
  </div>

  <div class="foot-title" style="left:763px;top:42px">Contact info</div>
  <div class="contact-row" style="top:108px">
    <svg width="12" height="17" viewBox="0 0 12 17"><path d="M6 0a6 6 0 0 0-6 6c0 4.5 6 11 6 11s6-6.5 6-11a6 6 0 0 0-6-6z" fill="#fff"/><circle cx="6" cy="6" r="2.2" fill="#151716"/></svg>
    <span>Address: 12569 Saint Lorem Ipsum is<br>simply dummy text of the prin</span>
  </div>
  <div class="contact-row" style="top:163px">
    <svg width="14" height="14" viewBox="0 0 14 14"><path d="M3 1l2 3-1.5 1.5a8 8 0 0 0 5 5L10 9l3 2-1 2.5C6 14 0 8 .5 2z" fill="#fff"/></svg>
    <span>Phone: +12 555 210-34-67<br>&nbsp;&nbsp;&nbsp;&nbsp;&nbsp;&nbsp;&nbsp;&nbsp;&nbsp;&nbsp;&nbsp;+12 555 210-34-68</span>
  </div>
  <div class="contact-row" style="top:225px">
    <svg width="14" height="11" viewBox="0 0 14 11"><rect width="14" height="11" fill="#fff"/><path d="M0 0l7 6 7-6" fill="none" stroke="#151716" stroke-width="1.3"/></svg>
    <span>E-mail: <a>Contact@LendALantern.org</a></span>
  </div>
  <div class="foot-title" style="left:763px;top:284px;font-size:16px">Follow Us</div>
  <div class="contact-row" style="top:316px;width:300px">
    <span>Lorem Ipsum is simply dummy text of the printing and typesetting industry.</span>
  </div>
  <svg class="abs" style="left:986px;top:375px" width="16" height="12" viewBox="0 0 16 12"><rect x=".5" y=".5" width="15" height="11" fill="none" stroke="#fff"/><path d="M.5 .5l7.5 6 7.5-6" fill="none" stroke="#fff"/></svg>
</footer>
<div class="subscribe"></div>

<div class="bottom-bar">
  <div class="copyright">Copyright 2014 - Lend a Lantern - All Rights Reserved</div>
  <div class="socials"><span></span><span></span><span></span><span></span><span></span></div>
</div>

</body>
</html>
```